Operator Qualification Testing Flyer

I have a 8x10 basic flyer that I created usin InDesign for one of our services our company provides. I would like to see more options for the layout and general design of the flyer. This flyer will be used as a template for the other services we provide. I will include the InDesign Folder with all the logos and images. Please feel free to use any logo design within the folder and you can change the font and/or colors as needed. I would like the final output in a Indesign package folder to be used in InDesign 2021

Target Market(s)

Business to Business marketing in the Oil and Gas industry

Font styles to use
Sans Serif

Colors
85cae6
85acd3
3377b5
0355a3
0792cd
ffffff
cedeed

Requirements
Must have
• I included/attached a couple of brochures styles that I do like.

```html
<!DOCTYPE html>
<html lang="en">
<head>
<meta charset="utf-8">
<title>Pipeline OQ Testing Flyer</title>
<link href="https://fonts.googleapis.com/css2?family=Archivo+Black&family=Arimo:wght@400;700&display=swap" rel="stylesheet">
<style>
  :root {
    --navy: #0355a3;
    --mid-blue: #3377b5;
    --bright-blue: #0792cd;
    --sky: #85cae6;
    --steel: #85acd3;
    --mist: #cedeed;
    --white: #ffffff;
    --ink: #1e2a36;
    --earth: #a9835a;
  }
  * { margin: 0; padding: 0; box-sizing: border-box; }
  html, body { width: 960px; height: 1200px; overflow: hidden; background: var(--white); }
  .flyer { position: relative; width: 960px; height: 1200px; overflow: hidden; background: var(--white); font-family: "Arimo", Arial, sans-serif; color: var(--ink); }
  .shapes { position: absolute; inset: 0; }

  .title-block { position: absolute; left: 56px; top: 352px; }
  .title {
    font-family: "Archivo Black", "Arial Black", sans-serif; font-size: 54px; line-height: 1.02;
    color: var(--white); letter-spacing: 1px;
  }
  .title .accent { color: var(--sky); }

  .column-left { position: absolute; left: 56px; top: 548px; width: 404px; }
  .panel-provide { position: absolute; left: 500px; top: 532px; width: 404px; padding: 26px 28px 24px; background: var(--mist); border-radius: 14px; border-top: 6px solid var(--bright-blue); }
  h2 { font-size: 22px; font-weight: 700; color: var(--navy); line-height: 1.2; margin-bottom: 8px; }
  p { font-size: 15px; line-height: 23px; margin-bottom: 10px; }
  .section-gap { margin-top: 22px; }

  .sign-photo { position: absolute; left: 56px; top: 952px; width: 184px; height: 184px; border-radius: 50%; border: 6px solid var(--white);
    background: radial-gradient(circle, #f2b31e 0%, #e6a214 58%, #1a1a1a 62%, #1a1a1a 100%); }

  .brand { position: absolute; left: 270px; top: 1088px; display: flex; align-items: center; gap: 12px; }
  .brand-dot { width: 18px; height: 18px; border-radius: 50%; background: var(--sky); }
  .brand-name { font-size: 24px; font-weight: 700; color: var(--white); line-height: 1; white-space: nowrap; }

  .contact { position: absolute; right: 56px; top: 1070px; color: var(--white); font-size: 20px; line-height: 34px; }
  .contact-line { display: flex; align-items: center; justify-content: flex-end; gap: 10px; }
  .contact-icon { width: 22px; height: 22px; }
</style>
</head>
<body>
<div class="flyer">
  <svg class="shapes" width="960" height="1200" viewBox="0 0 960 1200">
    <defs>
      <linearGradient id="site" x1="0" y1="0" x2="1" y2="1">
        <stop offset="0" stop-color="#8fb3c4"/>
        <stop offset="0.45" stop-color="#b08a5f"/>
        <stop offset="1" stop-color="#c2a07a"/>
      </linearGradient>
    </defs>
    <path role="img" aria-label="Aerial photo of an excavator beside a trench with blue pipelines and workers" d="M0 0 H960 V410 L0 490 Z" fill="url(#site)"/>
    <path d="M0 330 H560 L520 500 H0 Z" fill="var(--navy)"/>
    <path d="M560 330 H580 L540 500 H520 Z" fill="var(--bright-blue)"/>
    <path d="M0 1000 Q480 930 960 1000 V1200 H0 Z" fill="var(--bright-blue)"/>
    <path d="M0 1012 Q480 942 960 1012 V1200 H0 Z" fill="var(--navy)"/>
  </svg>

  <div class="title-block">
    <h1 class="title">PIPELINE <span class="accent">OQ</span><br>TESTING</h1>
  </div>

  <section class="column-left">
    <h2>What Is Operator Qualification?</h2>
    <p>Operator Qualifications (OQ) for DOT Oil/Gas Pipelines are requirements set by Department of Transportation (DOT) and Pipeline and Hazardous Materials Safety Administration (PHMSA). To assure safety in the transport of hazardous gases and liquids in the nation’s pipelines, pipeline operators who perform covered tasks must be qualified. Qualified means that an individual has been evaluated and can perform assigned covered tasks and recognize and react to abnormal operating conditions.</p>
    <h2 class="section-gap">What Are Covered Tasks?</h2>
    <p>Covered tasks are defined in an operator’s written plan which defines specific job functions or activities personnel are qualified to perform on a pipeline facility.</p>
  </section>

  <section class="panel-provide">
    <h2>What We Provide</h2>
    <p>Keystone Field Services Inc. utilizes NTCB pipeline program to administer OQ assessment testing on 127 covered tasks.</p>
    <p>Upon completion of OQ testing the information is first transferred to NTCB’s Registry System and automatically uploaded to SafeLedger.</p>
    <p>In addition to the benefits provided by SafeLedger’s database, the NTCB Registry System houses all the completion information allowing candidates to share their training information and employers to verify successful covered task and level completions.</p>
  </section>

  <div class="sign-photo" role="img" aria-label="Photo of a round yellow petroleum pipeline warning sign"></div>

  <div class="brand">
    <span class="brand-dot"></span>
    <span class="brand-name">Keystone Field Services Inc.</span>
  </div>

  <div class="contact">
    <div class="contact-line">555-014-2237
      <svg class="contact-icon" viewBox="0 0 24 24"><circle cx="12" cy="12" r="12" fill="var(--sky)"/><path d="M8 6.5 L10 6.5 L11 9.5 L9.8 10.6 Q11 13 13.4 14.2 L14.5 13 L17.5 14 L17.5 16 Q17 17.5 15.5 17.5 Q7 17 6.5 8.5 Q6.5 7 8 6.5 Z" fill="var(--navy)"/></svg>
    </div>
    <div class="contact-line">alex@keystonefield.co
      <svg class="contact-icon" viewBox="0 0 24 24"><circle cx="12" cy="12" r="12" fill="var(--sky)"/><rect x="6.5" y="8" width="11" height="8" rx="1" fill="none" stroke="var(--navy)" stroke-width="1.6"/><path d="M6.8 8.5 L12 12.5 L17.2 8.5" fill="none" stroke="var(--navy)" stroke-width="1.6"/></svg>
    </div>
  </div>
</div>
</body>
</html>
```